Webdesign für Gemeinschaftspraxis (13820)
Zielgruppe
Die Website ist für eine fachärztliche Gemeinschaftspraxis, die sich aus Internisten, Betriebsmedizinern, Präventionsärzten, Kardiologen, Allgemeinmedizinern und Phlebologen zusammensetzt.
Die Zielgruppe sind bestehende Patienten sowie potentielle Patienten.
Die Website soll informativ sein.
Aufgabenstellung
Die Website soll in schlichten Farben gehalten sein, die zum Logo und zu den Fotos passen.
Die Website soll als kurzer, informativer Auftritt dienen
Die gelieferten Fotos sollen verwendet werden.
Es soll eine Onepage-Website werden, die so aufgebaut ist, wie die Website unter dem folgenden Link: https://www.kolbenfeld-portal.de/

```html
<!DOCTYPE html>
<html lang="de">
<head>
<meta charset="utf-8">
<title>Gemeinschaftspraxis – Ärzte</title>
<link rel="stylesheet" href="https://fonts.googleapis.com/css2?family=Fira+Sans+Condensed:wght@400;500&family=Roboto:wght@400&display=swap">
<style>
  :root {
    --white: #ffffff;
    --ink: #111111;
    --navy: #14193a;
    --band: #e5e5e5;
    --bar: #535353;
    --photo: #dadada;
    --photo-deep: #9a9a9a;
  }
  * { margin: 0; padding: 0; box-sizing: border-box; }
  html, body { width: 1200px; height: 793px; overflow: hidden; background: var(--white); }
  body { position: relative; font-family: "Roboto", Arial, sans-serif; color: var(--ink); }

  .site-header {
    position: absolute; left: 0; top: 0; width: 1200px; height: 51px;
    background: var(--white); z-index: 2;
  }
  .brand {
    position: absolute; left: 228px; top: 17px;
    display: flex; align-items: center; gap: 5px;
    font-size: 10px; letter-spacing: 1px; color: var(--navy); font-weight: 400;
  }
  .brand-mark { width: 12px; height: 12px; background: var(--navy); }
  .main-nav a {
    position: absolute; top: 18px; line-height: 13px;
    font-size: 8px; letter-spacing: 1.9px; color: var(--ink); text-decoration: none;
  }
  .main-nav a.is-active {
    top: 15px; height: 20px; line-height: 17px; padding: 0 10px;
    border: 1.3px solid var(--ink);
  }

  .services {
    position: absolute; left: 0; top: 0; width: 1200px; height: 293px;
    background: linear-gradient(to bottom, #d8d8d8 51px, var(--band) 68px, var(--band));
  }
  .service-list {
    position: absolute; left: 198px; top: 37px; width: 558px; list-style: none;
    border: 1px solid var(--white); border-top: 0;
  }
  .service-list li {
    height: 26.3px; line-height: 25px; background: var(--bar);
    border-bottom: 1px solid var(--white);
    padding-left: 7px; color: var(--white);
    font-family: "Fira Sans Condensed", "Arial Narrow", sans-serif;
    font-size: 10.5px; font-weight: 500; letter-spacing: 1px;
  }

  .doctors-title {
    position: absolute; left: 198px; top: 343px;
    font-size: 15.5px; font-weight: 400; letter-spacing: 2.4px;
  }
  .doctor { position: absolute; top: 389px; width: 245px; }
  .doctor-photo {
    width: 172px; height: 228px;
    background: linear-gradient(to bottom, var(--photo) 0%, var(--photo) 45%, #b8b8b8 60%, var(--photo-deep) 100%);
  }
  .doctor-name {
    margin-top: 31px; font-size: 15.5px; font-weight: 400; letter-spacing: 2.4px;
  }
  .doctor-bio {
    margin-top: 13px; font-size: 8.7px; line-height: 11.8px; letter-spacing: 0.75px;
  }
</style>
</head>
<body>
  <header class="site-header">
    <div class="brand"><span class="brand-mark"></span>Praxis Lindenhof</div>
    <nav class="main-nav">
      <a style="left:348px">Praxis</a>
      <a style="left:427px">Leistungen</a>
      <a class="is-active" style="left:522px">Ärzte</a>
      <a style="left:603px">Teams</a>
      <a style="left:678px">Öffnungszeiten</a>
      <a style="left:808px">Kontakt</a>
    </nav>
  </header>

  <section class="services">
    <ul class="service-list">
      <li>EKG und Belastungs-EKG</li>
      <li>Langzeit-Blutdruckmessung</li>
      <li>Lungenfunktionstest</li>
      <li>Disease-Management-Programme (DMP)</li>
      <li>Ultraschall der Bauchorgane</li>
      <li>Ultraschall der Hirnversorgenden Arterien (Duplexsonografie)</li>
      <li>Spiroergometrie</li>
    </ul>
  </section>

  <h2 class="doctors-title">Ärzte</h2>

  <article class="doctor" style="left:198px">
    <div class="doctor-photo" role="img" aria-label="Porträtfoto Dr. Hollmann"></div>
    <h3 class="doctor-name" style="margin-top:34px">Dr. Hollmann</h3>
    <p class="doctor-bio" style="margin-top:11px">Lorem ipsum dolor sit amet, consectetuer adipiscing elit. Aenean commodo ligula eget dolor. Aenean massa. Cum sociis natoque penatibus et magnis dis parturient montes, nascetur ridiculus mus. Donec quam felis, ultricies nec, pellentesque eu, pretium quis, sem.</p>
  </article>

  <article class="doctor" style="left:495px">
    <div class="doctor-photo" role="img" aria-label="Porträtfoto Dr. Varenholt"></div>
    <h3 class="doctor-name">Dr. Varenholt</h3>
    <p class="doctor-bio">Lorem ipsum dolor sit amet, consectetuer adipiscing elit. Aenean commodo ligula eget dolor. Aenean massa. Cum sociis natoque penatibus et magnis dis parturient montes, nascetur ridiculus mus. Donec quam felis, ultricies nec, pellentesque eu, pretium quis, sem.</p>
  </article>

  <article class="doctor" style="left:794px">
    <div class="doctor-photo" role="img" aria-label="Porträtfoto Brückner"></div>
    <h3 class="doctor-name">Brückner</h3>
    <p class="doctor-bio">Lorem ipsum dolor sit amet, consectetuer adipiscing elit. Aenean commodo ligula eget dolor. Aenean massa. Cum sociis natoque penatibus et magnis dis parturient montes, nascetur ridiculus mus. Donec quam felis, ultricies nec, pellentesque eu, pretium quis, sem.</p>
  </article>
</body>
</html>
```